Invest in Real Estate housing and apartment development projects in Lima - Peru

Need a presentation for Grupo Venora, a top Real Estate developer from Peru who is looking for new leading investors such as Top Regional and Worldwide Real Estate funds and Regional Family offices and High Networth individuals to invest in Real Estate projects developed by/with Grupo Venora. Venora is focused on middle income apartments (housing) and has developed and delivered aprox 1400 apartments, and is currently developing and building 400 apartments. Venora currently has a potential to develop 1500 more apartments. And is looking to raise between US $50 and 60mm dollars a year in additional new investments, all focused on real estate housing (essentially vertical housing, apartments)
I have already some information and slides prepared with information regarding management fees, development and sales/marketing fees, success fees which are alligned to IRR of the project.

Target Market(s)

Real Estate investors in Latin America

Industry/Entity Type

Real Estate Development

Colors

Requirements
Must have
• Graphs and pictures of real estate projects. Data of housing market from Lima, capital of Peru compared to other top capitals in South America

```html
<!DOCTYPE html>
<html lang="es">
<head>
<meta charset="utf-8">
<title>Grupo Venora – Presentación</title>
<link href="https://fonts.googleapis.com/css2?family=Open+Sans:wght@400;600;700&family=Oswald:wght@500;600&display=swap" rel="stylesheet">
<style>
:root{
  --bg:#8a8588;
  --green:#3aa935;
  --green-dark:#2a8a27;
  --green-light:#8fd47a;
  --green-pale:#e4f2df;
  --ink:#333333;
  --muted:#777777;
  --grey-head:#555555;
  --white:#ffffff;
}
*{box-sizing:border-box;margin:0;padding:0}
html,body{width:1079px;height:1200px;overflow:hidden;background:var(--bg)}
body{position:relative;font-family:'Open Sans',Arial,sans-serif;color:var(--ink)}
.slide{position:absolute;width:286px;height:162px;background:var(--white);overflow:hidden;box-shadow:0 1px 3px rgba(0,0,0,.3)}
.slide-title{position:absolute;left:10px;top:10px;font-weight:700;font-size:5.8px;color:var(--ink);letter-spacing:.1px}
.slide-title::after{content:"";position:absolute;left:0;top:9px;width:14px;height:1px;background:var(--green)}
.photo{position:absolute}
.body-text{position:absolute;font-size:2.5px;line-height:1.45;color:var(--muted)}
.green{color:var(--green)}
.abs{position:absolute}
.label{font-size:2.7px;font-weight:700;color:var(--ink);text-align:center}
.tiny{font-size:2.1px;line-height:1.4;color:#888;text-align:center}
.display{font-family:'Oswald',Arial,sans-serif}
.col-head{color:#fff;font-size:2.6px;font-weight:700;text-align:center;padding:1.5px 0}
.col-list{font-size:1.9px;line-height:2.2;padding:1px 3px 3px}
.col-list.dark{background:#444;color:#ddd}
.col-list.lit{background:var(--green);color:#eaf6e6}
.table-list{font-size:2.4px;line-height:3.4;color:var(--muted);padding:2px 4px 3px}
</style>
</head>
<body>

<!-- Cover -->
<section class="slide" style="left:92px;top:70px">
  <div class="photo" role="img" aria-label="Faded photo of an apartment complex with gardens and pool" style="inset:0;background:linear-gradient(160deg,#f1f2ef 0%,#e3e8e0 40%,#d6e0d2 70%,#e7ebe4 100%)"></div>
  <div class="abs" style="left:20px;top:15px;display:flex;align-items:center;gap:3px">
    <span style="width:7px;height:7px;border-radius:50%;background:var(--green)"></span>
    <span style="font-weight:700;font-size:9px;color:var(--grey-head)">VENORA</span>
  </div>
  <div class="abs display" style="right:27px;top:100px;text-align:right;line-height:1.25">
    <div style="font-size:13px;color:var(--green);font-weight:600">PRESENTATION TILE</div>
    <div style="font-size:13px;color:var(--grey-head);font-weight:500">EDIT HERE</div>
  </div>
  <div class="abs" style="right:20px;top:102px;width:1.2px;height:34px;background:var(--green)"></div>
</section>

<!-- Why choose -->
<section class="slide" style="left:399px;top:67px">
  <h2 class="slide-title">POR QUÉ ELEGIR GRUPO VENORA</h2>
  <div class="abs" style="left:9px;top:35px;width:107px;height:105px;background:var(--green);padding:12px 14px;color:#fff;font-size:2.6px;line-height:1.5">
    <p>Somos una empresa de capital peruano dedicada al desarrollo de proyectos inmobiliarios con diseño innovador, moderno y funcional. Nuestra filosofía nos ha llevado a construir proyectos únicos, pensados en ser los nuevos hogares de las familias modernas y que puedan perdurar en el tiempo.</p>
    <p style="margin-top:4px">En Grupo Venora buscamos desarrollar proyectos trascendentes, basados en nuestros pilares de innovación y creatividad, permitiéndonos transformar espacios urbanos en propuestas únicas y funcionales para nuestros clientes.</p>
  </div>
  <div class="photo" role="img" aria-label="Team reviewing architectural floor plans on a table" style="left:116px;top:35px;width:161px;height:105px;background:linear-gradient(135deg,#cfc6bb 0%,#eeeeec 45%,#f4f4f2 65%,#bdb3a6 100%)"></div>
</section>

<!-- Our team -->
<section class="slide" style="left:708px;top:70px">
  <h2 class="slide-title">OUR TEAM</h2>
  <div class="abs" style="left:30px;top:42px;width:226px;display:flex;justify-content:space-between">
    <div style="width:50px;text-align:center">
      <div role="img" aria-label="Portrait of team member" style="width:41px;height:41px;border-radius:50%;margin:0 auto;background:radial-gradient(circle,#bdbdbd,#6d6d6d)"></div>
      <div style="margin-top:4px;font-size:3.6px;font-weight:700;color:var(--green)">LARA QUINN</div>
      <div style="font-size:2.5px;color:var(--muted)">General Manager</div>
    </div>
    <div style="width:50px;text-align:center">
      <div role="img" aria-label="Portrait of team member" style="width:41px;height:41px;border-radius:50%;margin:0 auto;background:radial-gradient(circle,#c59a82,#7b5a47)"></div>
      <div style="margin-top:4px;font-size:3.6px;font-weight:700;color:var(--green)">OWEN PIKE</div>
      <div style="font-size:2.5px;color:var(--muted)">Trainer Head</div>
    </div>
    <div style="width:50px;text-align:center">
      <div role="img" aria-label="Portrait of team member" style="width:41px;height:41px;border-radius:50%;margin:0 auto;background:radial-gradient(circle,#b98e6c,#6a4c38)"></div>
      <div style="margin-top:4px;font-size:3.6px;font-weight:700;color:var(--green)">RAFAEL SOTO</div>
      <div style="font-size:2.5px;color:var(--muted)">Finance</div>
    </div>
    <div style="width:50px;text-align:center">
      <div role="img" aria-label="Portrait of team member" style="width:41px;height:41px;border-radius:50%;margin:0 auto;background:radial-gradient(circle,#d3ab93,#85604c)"></div>
      <div style="margin-top:4px;font-size:3.6px;font-weight:700;color:var(--green)">IAN MARSH</div>
      <div style="font-size:2.5px;color:var(--muted)">Senior Trainer</div>
    </div>
  </div>
  <p class="body-text" style="left:24px;top:110px;width:238px;text-align:center">Lorem ipsum dolor sit amet, consectetur adipiscing elit, sed do eiusmod tempor incididunt ut labore et dolore magna aliqua. Ut enim ad minim veniam, quis nostrud exercitation ullamco laboris nisi ut aliquip ex ea commodo consequat. Duis aute irure dolor in reprehenderit in voluptate velit esse cillum dolore eu fugiat nulla pariatur. Excepteur sint occaecat cupidatat non proident, sunt in culpa qui officia deserunt mollit anim id est laborum.</p>
</section>

<!-- Mission vision values -->
<section class="slide" style="left:92px;top:252px">
  <div class="photo" role="img" aria-label="Smiling family at home" style="left:13px;top:15px;width:85px;height:68px;background:linear-gradient(135deg,#eadccd,#c49b7c 60%,#9a6f55)"></div>
  <div class="photo" role="img" aria-label="Family with arms raised under a sky with drawn house and car" style="left:102px;top:15px;width:85px;height:68px;background:linear-gradient(180deg,#4f86c2,#9dbfe0 65%,#6f9a4e)"></div>
  <div class="photo" role="img" aria-label="Mother and daughter on the grass" style="left:191px;top:15px;width:85px;height:68px;background:linear-gradient(170deg,#e0cfa8,#a9b65c 60%,#6f9a32)"></div>
  <div class="abs" style="left:13px;top:83px;width:263px;height:2px;background:var(--green)"></div>
  <div class="abs" style="left:13px;top:92px;width:85px">
    <div style="font-size:4px;font-weight:700;color:var(--green);text-align:center">MISIÓN</div>
    <p class="tiny" style="margin-top:3px">Ofrecemos innovadoras alternativas de vivienda, asegurando la mejor experiencia de compra, acompañando todo el ciclo de vida familiar de nuestros clientes.</p>
  </div>
  <div class="abs" style="left:102px;top:92px;width:85px">
    <div style="font-size:4px;font-weight:700;color:var(--green);text-align:center">VISIÓN</div>
    <p class="tiny" style="margin-top:3px">Somos una empresa desarrolladora de proyectos inmobiliarios con diseño innovador, moderno y funcional que construye valor y satisfacción a sus clientes, inversionistas y su entorno con un equipo emprendedor y de alto desempeño.</p>
  </div>
  <div class="abs" style="left:191px;top:92px;width:85px">
    <div style="font-size:4px;font-weight:700;color:var(--green);text-align:center">VALORES</div>
    <p class="tiny" style="margin-top:3px">Nos divertimos trabajando. Hacemos lo correcto con integridad y humildad. Promovemos el aprendizaje y desarrollo personal. Superamos los retos más complejos en equipo. Promovemos igualdad en oportunidades de crecimiento basados en nuestros méritos.</p>
  </div>
</section>

<!-- Our services -->
<section class="slide" style="left:399px;top:254px">
  <h2 class="slide-title">OUR SERVICES</h2>
  <svg class="abs" style="left:0;top:0" width="286" height="162" viewBox="0 0 286 162" aria-hidden="true">
    <g fill="#3aa935">
      <path d="M43 46h10l-5 5z M46 41h4v6h-4z"/><rect x="42" y="52" width="12" height="1.5"/>
      <circle cx="98" cy="46" r="5" fill="none" stroke="#3aa935" stroke-width="1.2"/><text x="98" y="47.5" font-size="4" text-anchor="middle" font-family="Open Sans">24</text>
      <path d="M142 44l6-4 6 4z"/><rect x="143" y="45" width="1.5" height="6"/><rect x="146.5" y="45" width="1.5" height="6"/><rect x="150" y="45" width="1.5" height="6"/><rect x="142" y="51.5" width="12" height="1.5"/>
      <ellipse cx="196" cy="45" rx="4.5" ry="3.5"/><ellipse cx="202" cy="48" rx="4" ry="3"/>
      <rect x="242" y="42" width="12" height="9" rx="1"/><path d="M242 42l6 5 6-5" fill="none" stroke="#fff" stroke-width=".8"/>
      <circle cx="48" cy="98" r="5" fill="none" stroke="#3aa935" stroke-width="1.2"/><path d="M48 95v3.5h2.5" fill="none" stroke="#3aa935" stroke-width="1"/>
      <circle cx="95" cy="96" r="3.5"/><circle cx="101" cy="100" r="2.5"/><circle cx="100" cy="94" r="2"/>
      <rect x="142" y="95" width="12" height="8" rx="1"/><circle cx="148" cy="99" r="2.5" fill="#fff"/><rect x="145" y="93" width="5" height="2"/>
      <rect x="193" y="94" width="11" height="9" fill="none" stroke="#3aa935" stroke-width="1.2"/><path d="M196 99l3 2 5-8" fill="none" stroke="#3aa935" stroke-width="1.2"/>
      <path d="M246 91h4v5h3l-5 5-5-5h3z"/><rect x="242" y="102" width="12" height="1.5"/>
    </g>
  </svg>
  <div class="abs" style="left:23px;top:58px;width:250px;display:grid;grid-template-columns:repeat(5,1fr);row-gap:40px;column-gap:4px">
    <div><div class="label">LOREM IPSUM</div><p class="tiny">Lorem ipsum dolor sit amet, consectetur adipiscing elit, sed do eiusmod tempor.</p></div>
    <div><div class="label">LOREM IPSUM</div><p class="tiny">Lorem ipsum dolor sit amet, consectetur adipiscing elit, sed do eiusmod tempor.</p></div>
    <div><div class="label">LOREM IPSUM</div><p class="tiny">Lorem ipsum dolor sit amet, consectetur adipiscing elit, sed do eiusmod tempor.</p></div>
    <div><div class="label">LOREM IPSUM</div><p class="tiny">Lorem ipsum dolor sit amet, consectetur adipiscing elit, sed do eiusmod tempor.</p></div>
    <div><div class="label">LOREM IPSUM</div><p class="tiny">Lorem ipsum dolor sit amet, consectetur adipiscing elit, sed do eiusmod tempor.</p></div>
    <div><div class="label">LOREM IPSUM</div><p class="tiny">Lorem ipsum dolor sit amet, consectetur adipiscing elit, sed do eiusmod tempor.</p></div>
    <div><div class="label">LOREM IPSUM</div><p class="tiny">Lorem ipsum dolor sit amet, consectetur adipiscing elit, sed do eiusmod tempor.</p></div>
    <div><div class="label">LOREM IPSUM</div><p class="tiny">Lorem ipsum dolor sit amet, consectetur adipiscing elit, sed do eiusmod tempor.</p></div>
    <div><div class="label">LOREM IPSUM</div><p class="tiny">Lorem ipsum dolor sit amet, consectetur adipiscing elit, sed do eiusmod tempor.</p></div>
    <div><div class="label">LOREM IPSUM</div><p class="tiny">Lorem ipsum dolor sit amet, consectetur adipiscing elit, sed do eiusmod tempor.</p></div>
  </div>
</section>

<!-- Building feature -->
<section class="slide" style="left:706px;top:254px">
  <h2 class="slide-title">EDIT TITLE HERE</h2>
  <div class="photo" role="img" aria-label="Modern white apartment building under a blue sky" style="left:9px;top:30px;width:113px;height:107px;background:linear-gradient(180deg,#2a7acb 0%,#5f9fd8 30%,#c9cdd1 55%,#a8adb2 80%,#6f8660 100%)"></div>
  <p class="body-text" style="left:134px;top:36px;width:142px;text-align:center">Lorem ipsum dolor sit amet, consectetur adipiscing elit, sed do eiusmod tempor incididunt ut labore et dolore magna aliqua. Ut enim ad minim veniam, quis nostrud exercitation ullamco laboris nisi ut aliquip ex ea commodo consequat. Duis aute irure dolor in reprehenderit in voluptate velit esse cillum dolore eu fugiat nulla pariatur. Excepteur sint occaecat cupidatat non proident, sunt in culpa qui officia deserunt mollit anim id est laborum sed do eiusmod tempor.</p>
  <svg class="abs" style="left:134px;top:94px" width="142" height="20" viewBox="0 0 142 20" aria-hidden="true">
    <g fill="#3aa935">
      <rect x="17" y="3" width="12" height="12" fill="none" stroke="#3aa935" stroke-width="1.3"/><path d="M23 5l-4 4h2.5v4h3v-4h2.5z"/>
      <rect x="64" y="10" width="2.5" height="5"/><rect x="68" y="7" width="2.5" height="8"/><rect x="72" y="4" width="2.5" height="11"/><path d="M63 8l5-4 4 2 5-4" fill="none" stroke="#3aa935" stroke-width="1"/>
      <rect x="112" y="2" width="8" height="13"/><rect x="120" y="7" width="6" height="8"/><rect x="114" y="4" width="1.5" height="1.5" fill="#fff"/><rect x="117" y="4" width="1.5" height="1.5" fill="#fff"/><rect x="114" y="8" width="1.5" height="1.5" fill="#fff"/><rect x="117" y="8" width="1.5" height="1.5" fill="#fff"/>
    </g>
  </svg>
  <div class="abs" style="left:134px;top:117px;width:142px;display:flex;justify-content:space-between">
    <p class="tiny" style="width:42px">Lorem ipsum dolor sit amet, consectetur adipiscing elit, sed do eiusmod tempor incididunt ut lab</p>
    <p class="tiny" style="width:42px">Lorem ipsum dolor sit amet, consectetur adipiscing elit, sed do eiusmod tempor incididunt ut lab</p>
    <p class="tiny" style="width:42px">Lorem ipsum dolor sit amet, consectetur adipiscing elit, sed do eiusmod tempor incididunt ut lab</p>
  </div>
</section>

<!-- Our focus -->
<section class="slide" style="left:92px;top:433px">
  <h2 class="slide-title">OUR FOCUS</h2>
  <div class="abs" style="left:0;top:25px;width:162px;height:124px;background:var(--green)"></div>
  <div class="photo" role="img" aria-label="Terrace with umbrella and sea view" style="left:162px;top:25px;width:124px;height:124px;background:linear-gradient(180deg,#bfe0ee 0%,#e6eef1 40%,#cfd4d6 75%,#9aa1a5 100%)"></div>
  <p class="abs" style="left:22px;top:47px;width:50px;font-size:3.6px;line-height:1.45;color:#fff;font-weight:700;text-align:center">Lorem ipsum dolor sit amet consectetur adipiscing elit. Cras bibendum mattis leo, ac efficitur ipsum lobortis non. Praesent vitae pulvinar <span style="font-weight:400">Lorem ipsum dolor sit amet consectetur adipiscing elit. Cras bibendum mattis leo.</span></p>
  <div class="abs" style="left:81px;top:51px;width:191px;height:69px;background:#fff;box-shadow:0 1px 3px rgba(0,0,0,.2)"></div>
  <svg class="abs" style="left:81px;top:51px" width="191" height="69" viewBox="0 0 191 69" aria-hidden="true">
    <g fill="#3aa935">
      <rect x="30" y="20" width="8" height="14"/><rect x="38" y="25" width="6" height="9"/><rect x="32" y="22" width="1.5" height="1.5" fill="#fff"/><rect x="35" y="22" width="1.5" height="1.5" fill="#fff"/><rect x="32" y="26" width="1.5" height="1.5" fill="#fff"/><rect x="35" y="26" width="1.5" height="1.5" fill="#fff"/>
      <rect x="89" y="22" width="14" height="12" rx="1.5"/><rect x="93" y="19" width="6" height="3" fill="none" stroke="#3aa935" stroke-width="1"/><path d="M95 25h2v2h2v2h-2v2h-2v-2h-2v-2h2z" fill="#fff"/>
      <path d="M147 27l2-6h12l2 6v7h-16z"/><circle cx="150" cy="30" r="1.3" fill="#fff"/><circle cx="160" cy="30" r="1.3" fill="#fff"/><rect x="150" y="22.5" width="10" height="3.5" fill="#fff"/>
    </g>
  </svg>
  <div class="abs" style="left:81px;top:93px;width:191px;display:flex;justify-content:space-around;padding:0 16px;font-size:4.2px;font-weight:700;color:var(--grey-head)">
    <span>LOREM</span><span>LOREM</span><span>LOREM</span>
  </div>
</section>

<!-- Six columns -->
<section class="slide" style="left:399px;top:433px">
  <h2 class="slide-title">EDIT TITLE HERE</h2>
  <div class="abs" style="left:16px;top:40px;width:258px;display:flex;justify-content:space-between">
    <div style="width:38px"><div role="img" aria-label="Business team in office" style="height:48px;background:linear-gradient(160deg,#7d93b2,#2f3d54)"></div><div class="col-head" style="background:#444">TITLE HERE</div><p class="col-list dark">• Lorem ipsum dolor sit<br>• Lorem ipsum dolor sit<br>• Lorem ipsum dolor sit<br>• Lorem ipsum dolor sit<br>• Lorem ipsum dolor sit<br>• Lorem ipsum dolor sit<br>• Lorem ipsum dolor sit</p></div>
    <div style="width:38px"><div role="img" aria-label="Pocket watch close-up" style="height:48px;background:linear-gradient(160deg,#d2ad86,#5a3b25)"></div><div class="col-head" style="background:var(--green)">TITLE HERE</div><p class="col-list lit">• Lorem ipsum dolor sit<br>• Lorem ipsum dolor sit<br>• Lorem ipsum dolor sit<br>• Lorem ipsum dolor sit<br>• Lorem ipsum dolor sit<br>• Lorem ipsum dolor sit<br>• Lorem ipsum dolor sit</p></div>
    <div style="width:38px"><div role="img" aria-label="Colleagues working at desks" style="height:48px;background:linear-gradient(160deg,#c2cedd,#4d5a6c)"></div><div class="col-head" style="background:#444">TITLE HERE</div><p class="col-list dark">• Lorem ipsum dolor sit<br>• Lorem ipsum dolor sit<br>• Lorem ipsum dolor sit<br>• Lorem ipsum dolor sit<br>• Lorem ipsum dolor sit<br>• Lorem ipsum dolor sit<br>• Lorem ipsum dolor sit</p></div>
    <div style="width:38px"><div role="img" aria-label="Businesswoman with headset" style="height:48px;background:linear-gradient(160deg,#dde3ea,#6c7a88)"></div><div class="col-head" style="background:var(--green)">TITLE HERE</div><p class="col-list lit">• Lorem ipsum dolor sit<br>• Lorem ipsum dolor sit<br>• Lorem ipsum dolor sit<br>• Lorem ipsum dolor sit<br>• Lorem ipsum dolor sit<br>• Lorem ipsum dolor sit<br>• Lorem ipsum dolor sit</p></div>
    <div style="width:38px"><div role="img" aria-label="Computer screen with charts" style="height:48px;background:linear-gradient(160deg,#e4e8ed,#5f6b78)"></div><div class="col-head" style="background:#444">TITLE HERE</div><p class="col-list dark">• Lorem ipsum dolor sit<br>• Lorem ipsum dolor sit<br>• Lorem ipsum dolor sit<br>• Lorem ipsum dolor sit<br>• Lorem ipsum dolor sit<br>• Lorem ipsum dolor sit<br>• Lorem ipsum dolor sit</p></div>
    <div style="width:38px"><div role="img" aria-label="Business meeting in glass office" style="height:48px;background:linear-gradient(160deg,#a9bdd1,#3d4b5a)"></div><div class="col-head" style="background:var(--green)">TITLE HERE</div><p class="col-list lit">• Lorem ipsum dolor sit<br>• Lorem ipsum dolor sit<br>• Lorem ipsum dolor sit<br>• Lorem ipsum dolor sit<br>• Lorem ipsum dolor sit<br>• Lorem ipsum dolor sit<br>• Lorem ipsum dolor sit</p></div>
  </div>
</section>

<!-- Lorem feature -->
<section class="slide" style="left:706px;top:434px">
  <h2 class="slide-title">EDIT TITLE HERE</h2>
  <div class="photo" role="img" aria-label="Glass skyscrapers seen from below against clouds" style="left:11px;top:30px;width:91px;height:103px;background:linear-gradient(200deg,#e6eef6 0%,#9fb3c9 35%,#556a85 70%,#2f3c50 100%)"></div>
  <div class="abs display" style="left:117px;top:37px;font-size:7px;font-weight:600;color:var(--green)">LOREM IPSUM</div>
  <p class="body-text" style="left:117px;top:48px;width:159px;text-align:justify">Lorem ipsum dolor sit amet consectetur adipiscing elit. Cras bibendum mattis leo, ac efficitur ipsum lobortis non. Praesent vitae pulvinar metus. Phasellus accumsan elementum condimentum. Nullam rutrum, tellus tincidunt scelerisque placerat, justo lectus luctus odio, varius auctor urna lacus sed nisl. Suspendisse at placerat sem. Duis tincidunt augue vel eros hendrerit tempus. Lorem ipsum dolor sit amet consectetur adipiscing elit. Cras bibendum mattis leo, ac efficitur ipsum lobortis non. Praesent vitae pulvinar metus. Phasellus accumsan Lorem ipsum dolor sit amet consectetur adipiscing elit. Cras bibendum mattis leo, ac efficitur ipsum lobortis non. Praesent vitae pulvinar metus. Phasellus accumsan elementum condimentum. Nullam rutrum, tellus tincidunt scelerisque placerat, justo lectus luctus odio, varius auctor urna lacus sed nisl. Suspendisse at placerat sem. Duis tincidunt augue vel eros hendrerit tempus. Lorem ipsum dolor sit amet consectetur adipiscing elit. Cras bibendum mattis leo.</p>
</section>

<!-- Industry grid -->
<section class="slide" style="left:92px;top:614px">
  <h2 class="slide-title">EDIT TITLE HERE</h2>
  <div class="photo" role="img" aria-label="City skyline at dusk with lit towers" style="left:0;top:30px;width:286px;height:132px;background:linear-gradient(180deg,#28509a 0%,#46689a 35%,#86765f 68%,#d99a3a 86%,#3a2a1c 100%)"></div>
  <div class="abs" style="left:23px;top:40px;width:241px;display:grid;grid-template-columns:repeat(4,1fr);gap:3px">
    <div style="height:47px;background:#fff;display:flex;flex-direction:column;justify-content:flex-end;padding-bottom:6px"><div class="label" style="font-weight:400;font-size:2.5px">LOREM IPSUM</div></div>
    <div style="height:47px;background:#fff;display:flex;flex-direction:column;justify-content:flex-end;padding-bottom:6px"><div class="label" style="font-weight:400;font-size:2.5px">LOREM IPSUM</div></div>
    <div style="height:47px;background:#fff;display:flex;flex-direction:column;justify-content:flex-end;padding-bottom:6px"><div class="label" style="font-weight:400;font-size:2.5px">LOREM IPSUM</div></div>
    <div style="height:47px;background:#fff;display:flex;flex-direction:column;justify-content:flex-end;padding-bottom:6px"><div class="label" style="font-weight:400;font-size:2.5px">LOREM IPSUM</div></div>
    <div style="height:47px;background:#fff;display:flex;flex-direction:column;justify-content:flex-end;padding-bottom:6px"><div class="label" style="font-weight:400;font-size:2.5px">LOREM IPSUM</div></div>
    <div style="height:47px;background:#fff;display:flex;flex-direction:column;justify-content:flex-end;padding-bottom:6px"><div class="label" style="font-weight:400;font-size:2.5px">LOREM IPSUM</div></div>
    <div style="height:47px;background:#fff;display:flex;flex-direction:column;justify-content:flex-end;padding-bottom:6px"><div class="label" style="font-weight:400;font-size:2.5px">LOREM IPSUM</div></div>
    <div style="height:47px;background:#fff;display:flex;flex-direction:column;justify-content:flex-end;padding-bottom:6px"><div class="label" style="font-weight:400;font-size:2.5px">LOREM IPSUM</div></div>
  </div>
  <svg class="abs" style="left:23px;top:40px" width="241" height="97" viewBox="0 0 241 97" aria-hidden="true">
    <g fill="#3aa935">
      <rect x="28" y="14" width="3" height="18"/><path d="M24 14h11l-5.5-6z"/><rect x="24" y="32" width="11" height="1.5"/>
      <path d="M84 20h14l-2 8h-10z"/><rect x="89" y="12" width="4" height="8"/><rect x="84" y="30" width="14" height="1.5"/>
      <rect x="150" y="16" width="1.5" height="16"/><path d="M150.7 16l-6-4M150.7 16l6-4M150.7 16v-7" stroke="#3aa935" stroke-width="1"/>
      <path d="M204 22h14l-3-6h-8z"/><circle cx="211" cy="13" r="3"/><rect x="210" y="22" width="2" height="10"/>
      <rect x="26" y="70" width="10" height="9"/><rect x="28" y="63" width="2" height="7"/><rect x="32" y="66" width="2" height="4"/>
      <path d="M83 78l14-12" stroke="#3aa935" stroke-width="2"/><rect x="86" y="70" width="3" height="9"/><rect x="82" y="78" width="10" height="1.5"/>
      <path d="M150 64l4 6h-8zM145 74h10l-5 6z" fill="none" stroke="#3aa935" stroke-width="1.3"/>
      <path d="M204 72l2-5h11l2 5v6h-15z"/><circle cx="207" cy="75" r="1.2" fill="#fff"/><circle cx="216" cy="75" r="1.2" fill="#fff"/>
    </g>
  </svg>
</section>

<!-- Timeline -->
<section class="slide" style="left:399px;top:614px">
  <h2 class="slide-title">TIMELINE</h2>
  <svg class="abs" style="left:0;top:0" width="286" height="162" viewBox="0 0 286 162" font-family="Open Sans" aria-hidden="true">
    <line x1="39" y1="126" x2="250" y2="126" stroke="#666" stroke-width=".8"/>
    <g stroke="#999" stroke-width=".5" stroke-dasharray="1 1">
      <line x1="39" y1="104" x2="39" y2="126"/><line x1="72" y1="92" x2="72" y2="126"/><line x1="107" y1="100" x2="107" y2="126"/><line x1="143" y1="92" x2="143" y2="126"/><line x1="178" y1="100" x2="178" y2="126"/><line x1="213" y1="92" x2="213" y2="126"/><line x1="250" y1="100" x2="250" y2="126"/>
    </g>
    <g fill="#fff" stroke="#3aa935" stroke-width=".9">
      <circle cx="39" cy="82" r="17"/><circle cx="72" cy="70" r="17"/><circle cx="107" cy="78" r="17"/><circle cx="143" cy="70" r="17"/><circle cx="178" cy="78" r="17"/><circle cx="213" cy="70" r="17"/><circle cx="250" cy="78" r="17"/>
    </g>
    <g fill="#3aa935">
      <circle cx="39" cy="98" r="5"/><circle cx="72" cy="86" r="5"/><circle cx="107" cy="94" r="5"/><circle cx="143" cy="86" r="5"/><circle cx="178" cy="94" r="5"/><circle cx="213" cy="86" r="5"/><circle cx="250" cy="94" r="5"/>
    </g>
    <g fill="#fff" font-size="3.2" font-weight="700" text-anchor="middle">
      <text x="39" y="99.2">2011</text><text x="72" y="87.2">2012</text><text x="107" y="95.2">2013</text><text x="143" y="87.2">2014</text><text x="178" y="95.2">2015</text><text x="213" y="87.2">2016</text><text x="250" y="95.2">2017</text>
    </g>
    <g fill="#333" font-size="3" font-weight="700" text-anchor="middle">
      <text x="39" y="75">Edit Title</text><text x="72" y="63">Edit Title</text><text x="107" y="71">Edit Title</text><text x="143" y="63">Edit Title</text><text x="178" y="71">Edit Title</text><text x="213" y="63">Edit Title</text><text x="250" y="71">Edit Title</text>
    </g>
    <g fill="#888" font-size="1.9" text-anchor="middle">
      <text x="39" y="79">There are many</text><text x="39" y="81.5">variations of text</text><text x="39" y="84">available here</text>
      <text x="72" y="67">There are many</text><text x="72" y="69.5">variations of text</text><text x="72" y="72">available here</text>
      <text x="107" y="75">There are many</text><text x="107" y="77.5">variations of text</text><text x="107" y="80">available here</text>
      <text x="143" y="67">There are many</text><text x="143" y="69.5">variations of text</text><text x="143" y="72">available here</text>
      <text x="178" y="75">There are many</text><text x="178" y="77.5">variations of text</text><text x="178" y="80">available here</text>
      <text x="213" y="67">There are many</text><text x="213" y="69.5">variations of text</text><text x="213" y="72">available here</text>
      <text x="250" y="75">There are many</text><text x="250" y="77.5">variations of text</text><text x="250" y="80">available here</text>
    </g>
    <g fill="#666"><circle cx="39" cy="126" r="1.6"/><circle cx="72" cy="126" r="1.6"/><circle cx="107" cy="126" r="1.6"/><circle cx="143" cy="126" r="1.6"/><circle cx="178" cy="126" r="1.6"/><circle cx="213" cy="126" r="1.6"/><circle cx="250" cy="126" r="1.6"/></g>
  </svg>
</section>

<!-- Team feature -->
<section class="slide" style="left:708px;top:618px">
  <h2 class="slide-title">EDIT TITLE HERE</h2>
  <p class="abs" style="left:15px;top:27px;font-size:2.8px;font-weight:600;color:var(--grey-head)">Lorem ipsum dolor sit amet, consectetur adipiscing elit. Aenean sed tempor lorem. Suspendisse</p>
  <div class="photo" role="img" aria-label="Business team joining hands in a huddle" style="left:19px;top:38px;width:145px;height:62px;background:linear-gradient(135deg,#eeece8,#a89f94 55%,#5a5650)"></div>
  <div class="abs" style="left:164px;top:38px;width:104px;height:62px;background:var(--green);padding:7px 12px;color:#fff">
    <div style="font-size:4px;font-weight:700">LOREM IPSUM</div>
    <p style="margin-top:4px;font-size:2.7px;line-height:1.45;text-align:justify">Lorem ipsum dolor sit amet, consectetur adipiscing elit. Aenean sed tempor lorem. Suspendisse varius enim id dolor euismod, quis condimentum risus blandit. Sed imperdiet dolor orci, at pulvinar sed pharetra et.</p>
  </div>
  <p class="body-text" style="left:15px;top:108px;width:256px;text-align:justify">Nunc consequat, massa vitae dignissim elementum, nisi magna tempor sapien, efficitur luctus metus dolor in enim. Ut placerat et purus eu porttitor. Maecenas quis velit enim. Suspendisse mollis diam et ligula laoreet, at commodo eros venenatis. Etiam elementum sollicitudin iaculis. Proin et congue sem, vitae ullamcorper risus. Sed in pretium erat, a finibus urna. Pellentesque habitant morbi tristique netus et malesuada fames ac turpis egestas.</p>
  <p class="body-text" style="left:15px;top:132px;width:256px;text-align:justify">Donec interdum nunc eu lacinia viverra. Praesent dapibus erat at elit eleifend consequat. Ut facilisis sem felis, vel tincidunt eros cursus eu. Vestibulum sed blandit lorem. In pretium quam euismod ipsum fermentum, ultrices semper tortor rhoncus. Sed non lorem enim. Quisque tincidunt nisl et euismod rutrum. Integer ut nibh magna.</p>
</section>

<!-- Text with photos -->
<section class="slide" style="left:92px;top:796px">
  <h2 class="slide-title">EDIT TITLE HERE</h2>
  <div class="abs" style="left:76px;top:34px;font-size:4px;font-weight:700;color:var(--ink)">Title here</div>
  <p class="body-text" style="left:26px;top:43px;width:74px;text-align:right;font-size:2.4px;line-height:1.4">Lorem ipsum dolor sit amet consectetur adipiscing elit. Cras bibendum mattis leo, ac efficitur ipsum lobortis non. Praesent vitae pulvinar metus. Phasellus accumsan elementum condimentum. Nullam rutrum, tellus tincidunt scelerisque placerat, justo lectus luctus odio, varius auctor urna lacus sed nisl. Suspendisse at placerat sem. Duis tincidunt augue vel eros hendrerit tempus. Lorem ipsum dolor sit amet consectetur adipiscing elit. Cras bibendum mattis leo, ac efficitur ipsum lobortis non. Praesent vitae pulvinar metus. Phasellus accumsan Lorem ipsum dolor sit Lorem ipsum dolor sit amet consectetur adipiscing elit. Cras bibendum mattis leo, ac efficitur ipsum lobortis non. Praesent vitae pulvinar metus. Phasellus accumsan Lorem ipsum dolor sit Lorem ipsum dolor sit amet consectetur adipiscing elit. Cras bibendum.</p>
  <div class="photo" role="img" aria-label="Aerial view of a coastal city with marina" style="left:114px;top:15px;width:82px;height:133px;background:linear-gradient(180deg,#c3d4e6 0%,#8699ad 30%,#5b7b90 58%,#3e6d4a 100%)"></div>
  <div class="photo" role="img" aria-label="Aerial view of a green park with a lake" style="left:201px;top:15px;width:74px;height:61px;background:linear-gradient(160deg,#8ab0d0,#4a8244 55%,#77925a)"></div>
  <div class="photo" role="img" aria-label="Crowded city street with buildings" style="left:201px;top:81px;width:74px;height:67px;background:linear-gradient(180deg,#d0d3d7,#86796f 60%,#4a3e3a)"></div>
</section>

<!-- Chart slide -->
<section class="slide" style="left:401px;top:794px">
  <h2 class="slide-title">EDIT TITLE HERE</h2>
  <div class="photo" role="img" aria-label="Modern glass office building with trees against a blue sky" style="left:16px;top:27px;width:254px;height:48px;background:linear-gradient(180deg,#3a82d2 0%,#a4c7ea 45%,#7b8895 75%,#4f7b3a 100%)"></div>
  <p class="body-text" style="left:16px;top:82px;width:136px;text-align:justify;font-size:2.4px">Lorem ipsum dolor sit amet consectetur adipiscing elit. Cras bibendum mattis leo, ac efficitur ipsum lobortis non. Praesent vitae pulvinar metus. Phasellus accumsan elementum condimentum. Nullam rutrum, tellus tincidunt scelerisque placerat, justo lectus luctus odio, varius auctor urna lacus sed nisl. Suspendisse at placerat sem. Duis tincidunt augue vel eros hendrerit tempus. Lorem ipsum dolor sit amet consectetur adipiscing elit. Cras bibendum mattis leo, ac efficitur ipsum lobortis non. Praesent vitae pulvinar metus. Phasellus accumsan Lorem ipsum dolor sit Lorem ipsum dolor sit amet consectetur adipiscing elit. Cras bibendum mattis leo, ac efficitur ipsum lobortis non. Praesent vitae pulvinar metus. Phasellus accumsan Lorem ipsum dolor sit Lorem ipsum dolor sit amet consectetur adipiscing elit. Cras bibendum</p>
  <svg class="abs" style="left:0;top:0" width="286" height="162" viewBox="0 0 286 162" font-family="Open Sans" aria-label="Pie chart of four segments: 40%, 25%, 20% and 15%" role="img">
    <path d="M187 118L187 89A29 29 0 0 1 204 141.5Z" fill="#6dd65c"/>
    <path d="M187 118L204 141.5A29 29 0 0 1 163.5 135Z" fill="#a6e896"/>
    <path d="M187 118L163.5 135A29 29 0 0 1 163.5 101Z" fill="#2f9a2a"/>
    <path d="M187 118L163.5 101A29 29 0 0 1 187 89Z" fill="#3fbf38"/>
    <g fill="#fff" font-size="3.6" font-weight="700" text-anchor="middle">
      <text x="202" y="117">40%</text><text x="186" y="137">25%</text><text x="172" y="120">20%</text><text x="178" y="103">15%</text>
    </g>
    <g stroke="#999" stroke-width=".5" fill="none">
      <path d="M200 92L206 89H240"/><path d="M214 108H240"/><path d="M214 127H240"/><path d="M205 140L212 145H240"/>
    </g>
    <g fill="#333" font-size="2.6" font-weight="700">
      <text x="243" y="90">Edit Title here</text><text x="243" y="109">Edit Title here</text><text x="243" y="128">Edit Title here</text><text x="243" y="146">Edit Title here</text>
    </g>
  </svg>
</section>

<!-- Table -->
<section class="slide" style="left:710px;top:796px">
  <h2 class="slide-title">EDIT TITLE HERE</h2>
  <div class="abs" style="left:9px;top:36px;width:268px;display:flex;justify-content:space-between">
    <div style="width:89px;background:var(--green-pale)">
      <div style="background:var(--green);color:#fff;font-size:3px;font-weight:700;text-align:center;padding:2.5px 0">Lorem ipsum dolor</div>
      <p class="table-list"><span class="green">•</span> Lorem ipsum dolor sit amet, consectetur<br><span class="green">•</span> Lorem ipsum dolor sit amet, consectetur<br><span class="green">•</span> Lorem ipsum dolor sit amet, consectetur<br><span class="green">•</span> Lorem ipsum dolor sit amet, consectetur<br><span class="green">•</span> Lorem ipsum dolor sit amet, consectetur<br><span class="green">•</span> Lorem ipsum dolor sit amet, consectetur<br><span class="green">•</span> Lorem ipsum dolor sit amet, consectetur<br><span class="green">•</span> Lorem ipsum dolor sit amet, consectetur<br><span class="green">•</span> Lorem ipsum dolor sit amet, consectetur<br><span class="green">•</span> Lorem ipsum dolor sit amet, consectetur<br><span class="green">•</span> Lorem ipsum dolor sit amet, consectetur</p>
    </div>
    <div style="width:88px;background:#eeeeee">
      <div style="background:var(--grey-head);color:#fff;font-size:3px;font-weight:700;text-align:center;padding:2.5px 0">Lorem ipsum dolor</div>
      <p class="table-list">• Lorem ipsum dolor sit amet, consectetur<br>• Lorem ipsum dolor sit amet, consectetur<br>• Lorem ipsum dolor sit amet, consectetur<br>• Lorem ipsum dolor sit amet, consectetur<br>• Lorem ipsum dolor sit amet, consectetur<br>• Lorem ipsum dolor sit amet, consectetur<br>• Lorem ipsum dolor sit amet, consectetur<br>• Lorem ipsum dolor sit amet, consectetur<br>• Lorem ipsum dolor sit amet, consectetur<br>• Lorem ipsum dolor sit amet, consectetur<br>• Lorem ipsum dolor sit amet, consectetur</p>
    </div>
    <div style="width:89px;background:var(--green-pale)">
      <div style="background:var(--green);color:#fff;font-size:3px;font-weight:700;text-align:center;padding:2.5px 0">Lorem ipsum dolor</div>
      <p class="table-list"><span class="green">•</span> Lorem ipsum dolor sit amet, consectetur<br><span class="green">•</span> Lorem ipsum dolor sit amet, consectetur<br><span class="green">•</span> Lorem ipsum dolor sit amet, consectetur<br><span class="green">•</span> Lorem ipsum dolor sit amet, consectetur<br><span class="green">•</span> Lorem ipsum dolor sit amet, consectetur<br><span class="green">•</span> Lorem ipsum dolor sit amet, consectetur<br><span class="green">•</span> Lorem ipsum dolor sit amet, consectetur<br><span class="green">•</span> Lorem ipsum dolor sit amet, consectetur<br><span class="green">•</span> Lorem ipsum dolor sit amet, consectetur<br><span class="green">•</span> Lorem ipsum dolor sit amet, consectetur<br><span class="green">•</span> Lorem ipsum dolor sit amet, consectetur</p>
    </div>
  </div>
</section>

<!-- Thank you -->
<section class="slide" style="left:402px;top:978px">
  <div class="photo" role="img" aria-label="Group of cheerful diverse people holding speech bubbles against a brick wall" style="inset:0;background:linear-gradient(90deg,#cdbda9 0%,#a98d72 45%,#8e5e45 70%,#b88d70 100%)"></div>
  <div class="abs" style="left:0;top:0;width:140px;height:162px;background:rgba(58,169,53,.88)"></div>
  <div class="abs" style="left:140px;top:0;width:30px;height:162px;background:rgba(58,169,53,.35)"></div>
  <div class="abs" style="left:52px;top:79px;font-size:10px;font-weight:600;color:#fff;letter-spacing:.2px">THANK YOU</div>
</section>

</body>
</html>
```